quorVale - website to pay membership association fee

The main purpose of this site it to allow a pre-registered user to be able to view the membership fees for their membership association and pay the same in one of the ways offered by the portal.
You are required to create a graphical project only for the logon functions as a user, while omitting the back end/administration ones that will be decided later
The site, besides being responsive must be very intuitive in its function. The graphics must be bright.

Number of Pages Required

4 page

Requirements
Must have
• i need to see template for
• 1. Home page
• 2. Page after login. People can se one or more bill to Pay and decide to see more details or to pay.
• 3. Page to Pay. Choose the desired payment method five alternative

```html
<!DOCTYPE html>
<html lang="en">
<head>
<meta charset="utf-8">
<title>quorVale – Membership Fees</title>
<link rel="stylesheet" href="https://fonts.googleapis.com/css2?family=Raleway:wght@600;700&family=Roboto:wght@400;500;700&display=swap">
<style>
  :root {
    --white: #ffffff;
    --accent: #00aeef;
    --field-border: #9a9a9a;
    --text-dark: #333333;
    --text-muted: #555555;
    --panel-dark: rgba(58, 58, 60, 0.78);
    --footer-bg: #f2f2f2;
    --footer-text: #666666;
    --photo-a: #3b3f42;
    --photo-b: #8b8f8c;
    --photo-c: #c9c9c6;
    --photo-d: #4f6b3a;
  }
  * { box-sizing: border-box; margin: 0; padding: 0; }
  html, body { width: 1200px; height: 677px; overflow: hidden; }
  body { position: relative; font-family: "Roboto", Arial, sans-serif; background: var(--footer-bg); }

  .hero { position: absolute; left: 0; top: 0; width: 1200px; height: 602px; overflow: hidden; }
  .hero-photo {
    position: absolute; inset: 0;
    background:
      radial-gradient(ellipse 260px 200px at 90px 120px, rgba(79,107,58,0.75), transparent 70%),
      radial-gradient(ellipse 360px 220px at 760px 540px, rgba(220,190,170,0.55), transparent 70%),
      linear-gradient(100deg, var(--photo-a) 0%, var(--photo-b) 35%, var(--photo-c) 60%, var(--photo-b) 85%, var(--photo-a) 100%);
  }

  .brand { position: absolute; left: 130px; top: 12px; font-family: "Raleway", Arial, sans-serif; font-weight: 700; font-size: 29px; color: var(--white); }
  .login-btn {
    position: absolute; left: 986px; top: 21px; width: 83px; height: 33px;
    border: 2px solid var(--white); color: var(--white);
    font-family: "Raleway", Arial, sans-serif; font-weight: 700; font-size: 13px;
    display: flex; align-items: center; justify-content: center;
  }

  .pay-form { position: absolute; left: 186px; top: 122px; width: 410px; height: 311px; background: rgba(255,255,255,0.94); }
  .field {
    position: absolute; left: 23px; width: 370px; height: 42px;
    border: 1px solid var(--field-border);
    display: flex; align-items: center; padding-left: 13px;
    font-size: 13.5px; color: var(--text-dark);
  }
  .field svg { width: 11px; height: 11px; margin-right: 11px; fill: #444; }
  .field-tax { top: 22px; }
  .field-email { top: 76px; }
  .field-member { top: 130px; }
  .consent { position: absolute; left: 23px; top: 195px; display: flex; align-items: center; font-size: 11.5px; color: var(--text-muted); }
  .consent-box { width: 16px; height: 16px; border-radius: 3px; background: var(--accent); margin-right: 9px; display: flex; align-items: center; justify-content: center; }
  .submit-btn {
    position: absolute; left: 23px; top: 239px; width: 370px; height: 46px;
    background: var(--accent); color: var(--white);
    font-weight: 700; font-size: 19px; display: flex; align-items: center; justify-content: center;
  }

  .about { position: absolute; left: 596px; top: 122px; width: 432px; height: 311px; background: var(--panel-dark); }
  .about-frame { position: absolute; left: 8px; top: 7px; right: 8px; bottom: 8px; border: 1px solid rgba(255,255,255,0.45); }
  .about-title { position: absolute; top: 72px; width: 100%; text-align: center; font-family: "Raleway", Arial, sans-serif; font-weight: 600; font-size: 24px; color: var(--white); }
  .about-rule { position: absolute; top: 109px; left: 201px; width: 29px; height: 2px; background: var(--white); }
  .about-text { position: absolute; top: 135px; left: 96px; width: 240px; text-align: center; font-size: 13px; line-height: 19.2px; color: var(--white); }

  .callout { position: absolute; top: 479px; width: 244px; height: 63px; }
  .callout svg { position: absolute; inset: 0; }
  .callout span {
    position: absolute; left: 0; top: 0; width: 244px; height: 48px;
    display: flex; align-items: center; justify-content: center;
    color: var(--white); font-weight: 700; font-size: 14.5px;
  }
  .callout-request { left: 186px; }
  .callout-forgotten { left: 482px; }
  .callout-assist { left: 782px; }

  .footer { position: absolute; left: 0; top: 602px; width: 1200px; height: 75px; background: var(--footer-bg); }
  .footer p { position: absolute; top: 32px; width: 100%; text-align: center; font-size: 10px; color: var(--footer-text); }
</style>
</head>
<body>
  <header class="hero">
    <div class="hero-photo" role="img" aria-label="Photo of hands typing on a keyboard while holding a payment card, with a plant in the background"></div>

    <div class="brand">quorVale</div>
    <div class="login-btn">LOGIN</div>

    <form class="pay-form">
      <div class="field field-tax">
        <svg viewBox="0 0 12 12"><rect x="0" y="2" width="12" height="1.5"/><rect x="0" y="5.25" width="12" height="1.5"/><rect x="0" y="8.5" width="12" height="1.5"/></svg>
        Tax identification code
      </div>
      <div class="field field-email">
        <svg viewBox="0 0 12 12"><path d="M0 2.5h12v1L6 7 0 3.5z"/><path d="M0 5l6 3.4L12 5v4.5H0z"/></svg>
        Email Address
      </div>
      <div class="field field-member">
        <svg viewBox="0 0 12 12"><circle cx="6" cy="3.2" r="2.6"/><path d="M1.5 11.5c0-3 2-4.8 4.5-4.8s4.5 1.8 4.5 4.8z"/></svg>
        Association Membership
      </div>
      <div class="consent">
        <div class="consent-box">
          <svg width="11" height="9" viewBox="0 0 11 9"><path d="M1 4.5l3 3L10 1" fill="none" stroke="#fff" stroke-width="2"/></svg>
        </div>
        Privacy Confirmation
      </div>
      <div class="submit-btn">SUBMIT</div>
    </form>

    <section class="about">
      <div class="about-frame"></div>
      <h2 class="about-title">About</h2>
      <div class="about-rule"></div>
      <p class="about-text">There are many variations of passages of Lorem Ipsum available, but the majority have suffered alteration in some form, by injected humour,</p>
    </section>

    <div class="callout callout-request">
      <svg viewBox="0 0 244 63"><path d="M1.5 1.5H242.5V61L226 46.5H1.5Z" fill="none" stroke="#fff" stroke-width="3"/></svg>
      <span>REQUEST FOR CREDENTIALS</span>
    </div>
    <div class="callout callout-forgotten">
      <svg viewBox="0 0 244 63"><path d="M1.5 1.5H242.5V61L226 46.5H1.5Z" fill="none" stroke="#fff" stroke-width="3"/></svg>
      <span>FORGOTTEN CREDENTIALS</span>
    </div>
    <div class="callout callout-assist">
      <svg viewBox="0 0 244 63"><path d="M1.5 1.5H242.5V61L226 46.5H1.5Z" fill="none" stroke="#fff" stroke-width="3"/></svg>
      <span>REQUEST FOR ASSISTANCE</span>
    </div>
  </header>

  <footer class="footer">
    <p>Copyrights @ 2017 All Rights Reserved</p>
  </footer>
</body>
</html>
```